Vantor Medica Innovative Business Card

Stunning business card. Background will be black. Letters in gold. Modern yet simple design that is attention grabbing. QR code leading to site. Attractive primarily to males ages 30 to 50 but also to females in same age range looking for beauty and mental health products

Target Market(s)

Males in the 30-50 age demographics

Industry/Entity Type

Pharmaceuticals selling erectile dysfunction and mens health medications

Contact Information for Business Card

www.vantormedica.example; (775) BUY-KELO; info@vantormedica.example

Colors
FFC000
F8CF3A
FAE287
FDF2CF
FEFAEE

Requirements
Must have
• Black business card with gold letters.
Nice to have
• perhaps just the logo or the "R" icon by itself on one side
Should not have
• too much content so it does not look busy

```html
<!DOCTYPE html>
<html lang="en">
<head>
<meta charset="utf-8">
<title>Vantor Medica Business Card</title>
<link href="https://fonts.googleapis.com/css2?family=Montserrat:wght@400;700&display=swap" rel="stylesheet">
<style>
  :root {
    --backdrop: #dddbdc;
    --card-black: #000000;
    --band-gold: #e3c24e;
    --band-gold-deep: #c9a53a;
    --text-gold: #e6c24a;
    --mark-gold: #cfa93c;
  }
  html, body {
    margin: 0;
    padding: 0;
    width: 1199px;
    height: 1200px;
    overflow: hidden;
    background: var(--backdrop);
  }
  .canvas {
    position: relative;
    width: 1199px;
    height: 1200px;
  }
  .card {
    position: absolute;
    left: 162px;
    width: 872px;
    height: 510px;
    display: block;
  }
  .card--front { top: 75px; }
  .card--back { top: 623px; }
  .brand-name {
    font-family: "Montserrat", sans-serif;
    font-weight: 700;
    fill: var(--mark-gold);
  }
  .contact-line {
    font-family: "Montserrat", sans-serif;
    font-weight: 400;
    font-size: 17.5px;
    fill: var(--text-gold);
  }
  .band { fill: var(--band-gold); }
  .cut { fill: var(--card-black); }
  .icon { fill: var(--text-gold); }
  .icon-line { fill: none; stroke: var(--card-black); stroke-width: 1.2; }
</style>
</head>
<body>
<main class="canvas">

  <!-- Front of card: name and contact details -->
  <svg class="card card--front" viewBox="0 0 698 408" aria-label="Business card front">
    <rect width="698" height="408" class="cut"/>
    <rect x="0" y="0" width="698" height="48" class="band"/>
    <polygon points="0,24 165,24 195,48 0,48" class="cut"/>
    <polygon points="290,48 315,48 365,14 340,14" class="cut"/>
    <polygon points="0,357 220,357 285,408 0,408" class="band"/>
    <polygon points="258,376 698,376 698,390 275,390" class="band"/>
    <polygon points="440,390 460,390 472,376 452,376" class="cut"/>

    <text class="brand-name" x="188" y="220" font-size="27" text-anchor="middle">Vantor Medica</text>

    <g class="contact">
      <g transform="translate(410,172)">
        <path class="icon" d="M2,1 L5,0 L7,4 L5,5.5 Q6.5,8.5 9,10 L10.5,8 L14,10 L13,13 Q5,13 1,4 Z"/>
      </g>
      <text class="contact-line" x="430" y="184">(775) BUY-KELO</text>

      <g transform="translate(410,204)">
        <circle cx="7" cy="7" r="6.5" class="icon"/>
        <ellipse cx="7" cy="7" rx="2.8" ry="6.5" class="icon-line"/>
        <line x1="0.5" y1="7" x2="13.5" y2="7" class="icon-line"/>
      </g>
      <text class="contact-line" x="430" y="216">www.vantormedica.example</text>

      <g transform="translate(410,237)">
        <rect x="0" y="0" width="14" height="10" class="icon"/>
        <polyline points="0.5,0.8 7,6 13.5,0.8" class="icon-line"/>
      </g>
      <text class="contact-line" x="430" y="248">info@vantormedica.example</text>
    </g>
  </svg>

  <!-- Back of card: decorative gold panel area and name -->
  <svg class="card card--back" viewBox="0 0 698 409" aria-label="Business card back">
    <defs>
      <linearGradient id="panel-tone" x1="0" y1="0" x2="0" y2="1">
        <stop offset="0" stop-color="var(--band-gold)"/>
        <stop offset="1" stop-color="var(--band-gold-deep)"/>
      </linearGradient>
    </defs>
    <rect width="698" height="409" class="cut"/>
    <rect class="decor-panel" x="0" y="0" width="208" height="409" fill="url(#panel-tone)"
          role="img" aria-label="Gold geometric panel decoration"/>
    <text class="brand-name" x="485" y="226" font-size="27" text-anchor="middle">Vantor Medica</text>
  </svg>

</main>
</body>
</html>
```